Business Cards for Retail/Sourcing Business.

We need a business cards for our company where it looks like:
TK
LV

VERTICAL, where the TK is over the LV. Then Under the TKLV would be name, address and website address. We want the P to be in the style of our original logo, which I uploaded.

Also, can we get a couple of designs with fun colors - especially for the letter head.

Target Market(s)

Old clients. Many of our clients or people we do business with are 40-50 plus. We are not an industry with many young people.

Industry/Entity Type

Business

Contact Information for Business Card

Front side is just says TKLV with name, title, address, and website below.

Font styles to use
Serif
Sans Serif
Decorative
Script

Requirements
Must have
• THE TKLV design with the P in the design of the logo
Nice to have
• Fun colors, new takes on the TKLV and any other additions that would be cool and make it pop

```html
<!DOCTYPE html>
<html lang="en">
<head>
<meta charset="utf-8">
<title>TKLV Business Card</title>
<link rel="stylesheet" href="https://fonts.googleapis.com/css2?family=Jost:wght@400;600&display=swap">
<style>
  :root {
    --paper: #ffffff;
    --ink: #0a0a0a;
    --frame: #1a1a1a;
    --mark: #0a0a0a;
  }
  html, body {
    margin: 0;
    padding: 0;
    width: 1200px;
    height: 900px;
    overflow: hidden;
    background: var(--paper);
  }
  .card {
    position: relative;
    box-sizing: border-box;
    width: 1200px;
    height: 900px;
    border: 2px solid var(--frame);
    background: var(--paper);
    font-family: "Jost", sans-serif;
    color: var(--ink);
    text-align: center;
  }
  .wordmark {
    position: absolute;
    left: 0;
    right: 0;
    top: 150px;
    margin: 0;
    font-family: "Jost", sans-serif;
    font-weight: 600;
    font-size: 150px;
    line-height: 150px;
    letter-spacing: 4px;
    color: var(--mark);
  }
  .wordmark span { display: block; }
  .contact {
    position: absolute;
    left: 0;
    right: 0;
    top: 518px;
    margin: 0;
    font-style: normal;
    font-size: 42px;
    line-height: 49px;
    letter-spacing: -0.5px;
  }
  .contact span { display: block; }
  .code {
    position: absolute;
    left: 0;
    right: 0;
    top: 758px;
    margin: 0;
    font-size: 30px;
    line-height: 36px;
  }
  .website {
    position: absolute;
    left: 0;
    right: 0;
    top: 810px;
    margin: 0;
    font-size: 31px;
    line-height: 38px;
  }
</style>
</head>
<body>
  <main class="card">
    <h1 class="wordmark"><span>TK</span><span>LV</span></h1>
    <address class="contact">
      <span class="contact-name">Marlon Vesper</span>
      <span class="contact-title">home sarangdor</span>
      <span class="contact-street">17 east 9th street</span>
      <span class="contact-city">LV, Lv</span>
    </address>
    <p class="code">100zz</p>
    <p class="website">www.tidewaygoodsltd.com</p>
  </main>
</body>
</html>
```